Technology, Futuristic Innovation & Artificial Intelligence

I am looking for something with Artificial Intelligence DNA strands....
Blue, black, with white dna strands........I like clean, crisp, professional and not busy look.................................................................................................................................................................................................................................................................................................................................................................................. Thanks!

Target Market(s)

Engineers and United States Government Contractors

Industry/Entity Type

Engineering

Contact Information for Business Card

I've uploaded my logo the certification logo.

Font styles to use
Serif

Colors
3176b5
33a6d7
ffffff

Requirements
Must have
• Name
• Title
• Address
• Phone number
• website name
• certification logo
Nice to have
• Something with Artificial Intelligence DNA strands......
• **Please note it would be nice to have the business card 3D or textured with raised images. Thanks
Should not have
• Please no feminine flowery designs....this is an engineering firm

```html
<!DOCTYPE html>
<html lang="en">
<head>
<meta charset="utf-8">
<title>Novalis Business Card</title>
<link rel="stylesheet" href="https://fonts.googleapis.com/css2?family=Oswald:wght@500;700&family=Open+Sans:wght@400;600&display=swap">
<style>
  :root {
    --page: #2b2b2d;
    --blue-deep: #2a3fb8;
    --blue-mid: #3176b5;
    --blue-bright: #33a6d7;
    --glow: #cfefff;
    --band: #3a3b3e;
    --band-dark: #1e1f21;
    --tooth: #0c0c0e;
    --white: #ffffff;
    --silver: #d9dde2;
    --badge: #c9a83a;
  }
  * { margin: 0; padding: 0; box-sizing: border-box; }
  html, body { width: 1200px; height: 900px; overflow: hidden; background: var(--page); }
  .canvas { position: relative; width: 1200px; height: 900px; }
  .card {
    position: absolute; left: 280px; width: 640px; height: 366px;
    border-radius: 22px; overflow: hidden;
    box-shadow: 0 18px 40px rgba(0,0,0,.55);
  }
  .card--front { top: 60px; }
  .card--back { top: 474px; }
  .circuit-field {
    position: absolute; inset: 0;
    background:
      radial-gradient(circle at 48% 50%, var(--glow) 0%, var(--blue-bright) 22%, transparent 55%),
      linear-gradient(120deg, var(--blue-bright) 0%, var(--blue-mid) 45%, var(--blue-deep) 100%);
  }
  .front-name {
    position: absolute; left: 0; right: 0; top: 138px; text-align: center;
    font: 700 72px/1 "Oswald", sans-serif; letter-spacing: 6px; color: var(--silver);
  }
  .front-name .mark-square {
    display: inline-block; width: 30px; height: 30px; background: var(--white);
    margin-right: 16px; vertical-align: 6px;
  }
  .front-web {
    position: absolute; right: 170px; top: 268px;
    font: 400 16px/1 "Open Sans", sans-serif; letter-spacing: 1px; color: var(--blue-deep);
  }
  .cert-badge {
    position: absolute; right: 40px; top: 26px; width: 74px; height: 74px;
    border-radius: 50%; background: var(--badge); border: 4px solid var(--blue-deep);
  }
  .back-band {
    position: absolute; left: 0; right: 0; top: 96px; height: 174px;
    background: linear-gradient(180deg, var(--band) 0%, var(--band-dark) 100%);
  }
  .teeth { position: absolute; left: 0; right: 0; height: 34px; }
  .teeth--top { top: 62px; }
  .teeth--bottom { top: 270px; }
  .brand {
    position: absolute; left: 36px; top: 150px; color: var(--silver);
  }
  .brand-name { font: 700 48px/1 "Oswald", sans-serif; letter-spacing: 5px; }
  .brand-name .mark-square {
    display: inline-block; width: 18px; height: 18px; background: var(--silver);
    margin-right: 10px; vertical-align: 6px;
  }
  .brand-tagline {
    font: 600 9px/1 "Open Sans", sans-serif; letter-spacing: 1.2px;
    margin-top: 6px; text-align: right;
  }
  .contact {
    position: absolute; left: 300px; top: 110px; width: 320px; color: var(--white);
    font: 400 13px/1.35 "Open Sans", sans-serif;
  }
  .contact-name { font: 700 26px/1.1 "Oswald", sans-serif; letter-spacing: 1px; margin-bottom: 8px; }
  .contact-name .title { font-size: 18px; margin-left: 6px; }
  .contact-line { display: flex; align-items: center; gap: 7px; margin-bottom: 4px; }
  .contact-line svg { flex: none; }
  .naics { font-size: 11px; margin-top: 6px; color: var(--silver); }
</style>
</head>
<body>
<main class="canvas">

  <section class="card card--front">
    <div class="circuit-field" role="img" aria-label="Glowing blue circuit-board trace pattern"></div>
    <div class="cert-badge" role="img" aria-label="Certification badge"></div>
    <div class="front-name"><span class="mark-square"></span>NOVALIS</div>
    <div class="front-web">WWW.NOVALISGROUP.ORG</div>
  </section>

  <section class="card card--back">
    <div class="circuit-field" role="img" aria-label="Glowing blue circuit-board trace pattern"></div>
    <svg class="teeth teeth--top" width="640" height="34" viewBox="0 0 640 34">
      <defs><pattern id="toothTop" width="22" height="34" patternUnits="userSpaceOnUse"><rect x="4" y="0" width="12" height="34" fill="#0c0c0e"/></pattern></defs>
      <rect width="640" height="34" fill="url(#toothTop)"/>
    </svg>
    <div class="back-band"></div>
    <svg class="teeth teeth--bottom" width="640" height="34" viewBox="0 0 640 34">
      <defs><pattern id="toothBottom" width="22" height="34" patternUnits="userSpaceOnUse"><rect x="4" y="0" width="12" height="34" fill="#0c0c0e"/></pattern></defs>
      <rect width="640" height="34" fill="url(#toothBottom)"/>
    </svg>

    <div class="brand">
      <div class="brand-name"><span class="mark-square"></span>NOVALIS</div>
      <div class="brand-tagline">ENGINEERING WHAT COMES NEXT</div>
    </div>

    <div class="contact">
      <div class="contact-name">JOAN MERCER<span class="title">CEO</span></div>
      <div class="contact-line">
        <svg width="14" height="12" viewBox="0 0 14 12"><rect x="0.5" y="0.5" width="13" height="11" fill="none" stroke="#33a6d7"/><path d="M0.5 0.5 L7 6 L13.5 0.5" fill="none" stroke="#33a6d7"/></svg>
        jmercer@novalisgroup.org
      </div>
      <div class="contact-line">
        <svg width="14" height="14" viewBox="0 0 14 14"><path d="M3 1 L5.5 1 L6.5 4 L5 5.5 C6 7.5 7 8.5 8.5 9 L10 7.5 L13 8.5 L13 11 C13 12 12 13 11 13 C5.5 12.5 1.5 8.5 1 3 C1 2 2 1 3 1 Z" fill="#33a6d7"/></svg>
        555.201.0147
      </div>
      <div class="contact-line">
        <svg width="12" height="16" viewBox="0 0 12 16"><path d="M6 0 C2.7 0 0 2.6 0 5.8 C0 10 6 16 6 16 C6 16 12 10 12 5.8 C12 2.6 9.3 0 6 0 Z" fill="#33a6d7"/><circle cx="6" cy="6" r="2.2" fill="#1e1f21"/></svg>
        1820 Harbor Mill Road, Clearwater, SC 29000
      </div>
      <div class="naics">NAICS: 3342-20/50/90, 5182-10/20/60, 5415-11, 5419-30, 6117-10, 8112-10/20/40, 8113-10</div>
    </div>
  </section>

</main>
</body>
</html>
```